Flooring Billboard Highlighting Large In Stock Inventory

Looking to create a billboard that primarily highlights our logo but also calls out our large in stock inventory and has the city we are located in and phone number at the bottom. Looking for a professional looking design, that is simplistic yet informative.

Location: Cedar Hollow, Near Exit 114

Phone: (715) 381-6094

Website: www.plankhavenstore.example

Products: Carpet, Hardwood, Laminate, Vinyl, Luxury Vinyl Plank & Window Treatments

Callouts:
-Free Estimates
-Wisconsin's In Stock Flooring Store
-Slogan: "Big city selection, small town service"

Target Market(s)

Home buyers, DIY'ers, Remoderls, designers

Industry/Entity Type

Flooring, Construction

Font styles to use
Serif

Requirements
Must have
• My logo, location, phone number and call out our large in stock inventory
Nice to have
• Call out the products we have and our slogan

```html
<!DOCTYPE html>
<html lang="en">
<head>
<meta charset="utf-8">
<title>Plank Haven Billboard</title>
<link href="https://fonts.googleapis.com/css2?family=Nunito:wght@400;600;700;800;900&family=Quicksand:wght@400;500&display=swap" rel="stylesheet">
<style>
  :root {
    --teal: #168f93;
    --rust: #c0632b;
    --ink: #2c2c2c;
    --strip: #f0f0f0;
    --paper: #ffffff;
    --backdrop: #444444;
  }
  * { margin: 0; padding: 0; box-sizing: border-box; }
  html, body { width: 1059px; height: 1200px; overflow: hidden; background: var(--backdrop); }
  .billboard {
    position: absolute; left: 68px; top: 469px;
    width: 923px; height: 261px;
    background: var(--paper);
    font-family: "Nunito", sans-serif;
    overflow: hidden;
  }
  .brand {
    position: absolute; left: 30px; top: 30px; width: 300px; height: 140px;
    display: flex; align-items: center; gap: 14px;
  }
  .brand-mark { width: 34px; height: 34px; background: var(--teal); flex: none; }
  .brand-name {
    font-family: "Quicksand", sans-serif; font-weight: 500;
    color: var(--rust); font-size: 58px; line-height: 1; letter-spacing: 0.5px;
  }
  .divider { position: absolute; top: 37px; width: 1px; height: 125px; background: var(--teal); }
  .divider.first { left: 351px; }
  .divider.second { left: 643px; }
  .headline { position: absolute; left: 392px; top: 24px; font-weight: 900; line-height: 1; }
  .headline .region { color: var(--rust); font-size: 24px; display: block; margin-bottom: 4px; }
  .headline .claim { color: var(--teal); font-size: 40px; display: block; line-height: 38px; }
  .ribbon { position: absolute; left: 764px; top: 0; }
  .slogan { position: absolute; left: 650px; width: 258px; top: 50px; text-align: center; }
  .slogan .line-one { font-family: "Quicksand", sans-serif; font-weight: 500; color: var(--rust); font-size: 25px; line-height: 27px; display: block; }
  .slogan .line-two { font-weight: 800; color: var(--teal); font-size: 22px; line-height: 24px; display: block; }
  .location {
    position: absolute; left: 701px; top: 120px; width: 155px; height: 62px;
    background: var(--rust); border-radius: 10px 10px 0 0;
    color: var(--paper); font-family: "Quicksand", sans-serif; font-weight: 500;
    font-size: 19px; line-height: 20px; text-align: center; padding-top: 10px;
    white-space: nowrap;
  }
  .products {
    position: absolute; left: 0; top: 182px; width: 100%; height: 33px;
    background: var(--strip);
    display: flex; align-items: center; justify-content: space-between;
    padding: 0 28px 0 30px; list-style: none;
    font-weight: 700; font-size: 15px; color: var(--ink);
  }
  .products li::before { content: "•"; color: var(--rust); margin-right: 10px; }
  .contact-bar { position: absolute; left: 0; top: 215px; width: 100%; height: 46px; display: flex; }
  .estimates {
    width: 222px; background: var(--rust); color: var(--paper);
    font-weight: 900; font-size: 23px; display: flex; align-items: center; justify-content: center;
  }
  .bar-gap { width: 6px; background: var(--paper); }
  .contact {
    flex: 1; background: var(--teal); color: var(--paper);
    display: flex; align-items: center; padding-left: 14px; gap: 10px;
    font-weight: 700; font-size: 29px; white-space: nowrap;
  }
  .contact svg { flex: none; }
  .contact .phone { margin-right: 16px; }
  .contact .web { font-size: 24px; }
</style>
</head>
<body>
  <section class="billboard">
    <div class="brand">
      <span class="brand-mark"></span>
      <span class="brand-name">Plank<br>Haven</span>
    </div>

    <span class="divider first"></span>

    <h1 class="headline">
      <span class="region">WISCONSIN'S</span>
      <span class="claim">IN STOCK</span>
      <span class="claim">FLOORING</span>
      <span class="claim">STORE</span>
    </h1>

    <span class="divider second"></span>

    <svg class="ribbon" width="30" height="44" viewBox="0 0 30 44" aria-hidden="true">
      <polygon points="0,0 30,0 30,44 15,38 0,44" fill="var(--teal)"/>
    </svg>

    <p class="slogan">
      <span class="line-one">Big city selection,</span>
      <span class="line-two">Small town service</span>
    </p>

    <p class="location">Cedar Hollow,<br>Near Exit 114</p>

    <ul class="products">
      <li>CARPET</li>
      <li>HARDWOOD</li>
      <li>LAMINATE</li>
      <li>VINYL</li>
      <li>LUXURY VINYL PLANK &amp;</li>
      <li>WINDOW TREATMENTS</li>
    </ul>

    <div class="contact-bar">
      <div class="estimates">FREE ESTIMATES</div>
      <div class="bar-gap"></div>
      <div class="contact">
        <svg width="18" height="26" viewBox="0 0 18 26" aria-hidden="true">
          <path d="M5 2 L9 2 L10 8 L7 10 Q7 16 10 19 L13 17 L17 21 L15 24 Q4 24 3 12 Q3 5 5 2 Z" fill="none" stroke="var(--paper)" stroke-width="2" stroke-linejoin="round"/>
        </svg>
        <span class="phone">(715) 381-6094</span>
        <svg width="22" height="22" viewBox="0 0 22 22" aria-hidden="true">
          <g fill="none" stroke="var(--paper)" stroke-width="1.6">
            <circle cx="11" cy="11" r="9"/>
            <ellipse cx="11" cy="11" rx="4" ry="9"/>
            <line x1="2" y1="11" x2="20" y2="11"/>
            <line x1="11" y1="2" x2="11" y2="20"/>
            <path d="M4 6 H18 M4 16 H18"/>
          </g>
        </svg>
        <span class="web">www.plankhavenstore.example</span>
      </div>
    </div>
  </section>
</body>
</html>
```